October Billboard TX

Billboard - creative design using company colors. Previous billboard graphic is included for reference along with a rough example of the requested "less busy" design. Required graphics for the simple billboard design are also included in the upload. Billboard dimensions are attached. Need this design ASAP!

```html
<!DOCTYPE html>
<html lang="en">
<head>
<meta charset="utf-8">
<title>Bright Sprouts Eye Center – Billboard</title>
<link rel="stylesheet" href="https://fonts.googleapis.com/css2?family=Sniglet:wght@400;800&family=Poppins:wght@500;600&display=swap">
<style>
  :root {
    --stage: #b0b0b0;
    --brand-blue: #0a6fc1;
    --navy: #16294a;
    --red: #e31d25;
    --yellow: #fff25c;
    --white: #ffffff;
    --black: #0b0b0b;
    --photo-a: #f2d3b8;
    --photo-b: #f6e36a;
  }
  * { margin: 0; padding: 0; box-sizing: border-box; }
  html, body { width: 1200px; height: 746px; overflow: hidden; background: var(--stage); }
  .billboard {
    position: absolute; left: 97px; top: 111px; width: 1006px; height: 524px;
    background: var(--brand-blue); overflow: hidden;
    box-shadow: 0 10px 24px rgba(0,0,0,.35);
    font-family: "Sniglet", "Poppins", sans-serif; font-weight: 800;
  }
  .corner-wave { position: absolute; left: 0; top: 0; }
  .brand-name {
    position: absolute; left: 48px; top: 40px; width: 300px;
    color: var(--brand-blue); font-size: 32px; line-height: 1; text-transform: uppercase;
    display: flex; align-items: center; gap: 10px;
  }
  .brand-name .dot { width: 22px; height: 22px; border-radius: 50%; background: var(--brand-blue); flex: none; }
  .brand-name small { display: block; font-size: 16px; margin-top: 6px; text-transform: none; color: var(--black); }
  .audience {
    position: absolute; left: 522px; top: 44px;
    display: grid; grid-template-columns: 188px auto; row-gap: 14px;
    list-style: none; color: var(--yellow); font-size: 24px; line-height: 28px; text-transform: uppercase;
  }
  .audience li { display: flex; align-items: center; gap: 10px; white-space: nowrap; }
  .testimonial {
    position: absolute; left: 70px; top: 190px; width: 560px; color: var(--white);
  }
  .testimonial .open-mark { display: block; color: var(--red); font-size: 60px; line-height: 34px; height: 30px; }
  .testimonial blockquote { font-size: 26px; line-height: 36px; text-transform: uppercase; white-space: nowrap; }
  .testimonial .close-mark {
    display: inline-block; color: var(--red); font-size: 60px; line-height: 36px; height: 36px;
    vertical-align: top; margin-left: 10px; transform: translateY(6px);
  }
  .testimonial cite {
    display: block; width: 480px; text-align: right; margin-top: 10px;
    font: 600 20px "Poppins", sans-serif; font-style: normal; color: var(--yellow);
  }
  .footer-band {
    position: absolute; left: 0; top: 413px; width: 620px; height: 111px; background: var(--white);
  }
  .footer-band::before {
    content: ""; position: absolute; left: 0; top: -12px; width: 100%; height: 12px;
    background: radial-gradient(circle at 12px 12px, var(--white) 11.5px, transparent 12px) repeat-x;
    background-size: 24px 12px;
  }
  .contact { position: absolute; left: 46px; top: 8px; }
  .contact .label {
    display: inline-block; background: var(--black); color: var(--white);
    font: 500 17px/34px "Poppins", sans-serif; padding: 0 10px; border-radius: 18px; width: 230px; text-align: center;
  }
  .contact .phone { display: block; font: 600 31px/42px "Poppins", sans-serif; color: var(--brand-blue); margin-top: 2px; }
  .spanish { position: absolute; left: 315px; top: 14px; color: var(--red); font-size: 27px; line-height: 34px; text-transform: uppercase; }
  .family-photo {
    position: absolute; left: 567px; top: 197px; width: 439px; height: 327px;
    background: radial-gradient(ellipse at 65% 45%, var(--photo-a), #d8a98a 55%, var(--photo-b) 95%);
    border-radius: 200px 0 0 0;
  }
  .kids-badge {
    position: absolute; left: 633px; top: 141px; width: 164px; height: 164px; border-radius: 50%;
    background: var(--yellow); border: 10px solid var(--red);
    display: flex; align-items: center; justify-content: center; text-align: center;
    color: var(--navy); font-size: 40px; line-height: 42px; text-transform: uppercase;
  }
</style>
</head>
<body>
<main class="billboard">
  <svg class="corner-wave" width="600" height="180" viewBox="0 0 600 180" aria-hidden="true">
    <path d="M0 0 H567 C470 20 430 150 279 168 H0 Z" fill="var(--white)"/>
    <path d="M567 0 C470 20 430 150 279 168" fill="none" stroke="var(--red)" stroke-width="6"/>
  </svg>

  <div class="brand-name"><span class="dot"></span><span>Bright Sprouts<br>Eye Center<small>of El Paso</small></span></div>

  <ul class="audience">
    <li><svg width="24" height="24" viewBox="0 0 24 24" aria-hidden="true"><circle cx="12" cy="12" r="10" fill="none" stroke="var(--yellow)" stroke-width="2.5"/><path d="M7 12l4 4 8-10" fill="none" stroke="var(--yellow)" stroke-width="3" stroke-linecap="round"/></svg>Newborns</li>
    <li><svg width="24" height="24" viewBox="0 0 24 24" aria-hidden="true"><circle cx="12" cy="12" r="10" fill="none" stroke="var(--yellow)" stroke-width="2.5"/><path d="M7 12l4 4 8-10" fill="none" stroke="var(--yellow)" stroke-width="3" stroke-linecap="round"/></svg>Toddlers</li>
    <li><svg width="24" height="24" viewBox="0 0 24 24" aria-hidden="true"><circle cx="12" cy="12" r="10" fill="none" stroke="var(--yellow)" stroke-width="2.5"/><path d="M7 12l4 4 8-10" fill="none" stroke="var(--yellow)" stroke-width="3" stroke-linecap="round"/></svg>Infants</li>
    <li><svg width="24" height="24" viewBox="0 0 24 24" aria-hidden="true"><circle cx="12" cy="12" r="10" fill="none" stroke="var(--yellow)" stroke-width="2.5"/><path d="M7 12l4 4 8-10" fill="none" stroke="var(--yellow)" stroke-width="3" stroke-linecap="round"/></svg>Tweens &amp; Teens</li>
  </ul>

  <figure class="testimonial">
    <span class="open-mark" aria-hidden="true">&ldquo;</span>
    <blockquote>I take my child to El Paso's most<br>qualified and experienced<br>pediatric eye doctor<span class="close-mark" aria-hidden="true">&rdquo;</span></blockquote>
    <cite>M. Reyes</cite>
  </figure>

  <div class="family-photo" role="img" aria-label="Photo of a smiling mother hugging her young daughter, who wears red glasses and a yellow headband"></div>

  <div class="kids-badge">Kids<br>only</div>

  <section class="footer-band">
    <div class="contact">
      <span class="label">FOR APPOINTMENTS CALL</span>
      <span class="phone">(915) 555-0142</span>
    </div>
    <p class="spanish">La doctora<br>habla español</p>
  </section>
</main>
</body>
</html>
```